Website Creation for Bloom Course 2025 by Tom Kessick "A Pilot Beyond Every Storm"

Project Title: "Bloom" Course Design Brief – Website design Build on Tilda
Client: Pine and Lantern Academy
Course Title: Bloom by Tom Kessick – A Pilot Beyond Every Storm
Logo: Tom Kessick Logo
Course price: TBA
Overview:
We are seeking a designer to create cohesive and professional design assets for a new online course called Bloom. This transformative program combines neuroscience, emotional wellness, and ancient meditation practices to guide users through a journey of self-healing. We want the design to feel scientific yet spiritual, with clean, modern aesthetics that also convey depth and transformation. We use Tilda as our website builder so we need a design that can be easily transposed to that platform.
We require a visually compelling and dynamic banner image for the course webpage hero section (desktop and mobile versions)
We also require 7 x Individual thumbnail designs for each chakra meditation that will accompany the course with a workbook that will be designed in house (aligned with energy centre themes / Solfeggio frequencies / cosmic and sacred geometry)
Visual Direction:
• Clean, modern design with dark elements that balance science and spirituality.
• Soft gradients, energetic colors for chakras, and subtle abstract patterns or sacred geometry.
• Imagery could include brain neural networks, energy centres, or serene meditative figures and sacred geometry.
Course Themes to Inspire Design:
• Neuroplasticity and brain rewiring
• Emotional trauma and healing
• Meditation and Solfeggio frequencies
• Mind-body-spirit connection
• Empowerment and transformation
Lesson Breakdown:
• Lesson 1: The Science of Meditation & the Mind-Body Connection
• Lesson 2: Tom Kessick’s Personal Healing & Neuroplasticity
• Lesson 3: Emotional Stress and Disease
• Lesson 4: SLR (Silver Lattice Release) Process
• Lesson 5: Solfeggio Frequencies & Chakra Healing
Target Audience:
Adult women 40 to 60 years old interested in healing illness, improving mental health, improving relationships, improving personal development, alternative healing, and meditation.

self development, meditation, healing

1 page

• futurapt

• branding copy used with relevant imagery and brand colours Stone #FAF0EA Sand #E2B9A5 Steel Blue #4F5266 Navy #2B243A Black: #000000 and Futura PT font
• chakra symbols and cosmic aesthetics with informational psychographics
• bright bold colours that don't match our branding

```html
<!DOCTYPE html>
<html lang="en">
<head>
<meta charset="utf-8">
<title>Bloom by Tom Kessick</title>
<link rel="stylesheet" href="https://fonts.googleapis.com/css2?family=Inter:wght@400;500;600;700&family=Playfair+Display:ital,wght@0,500;0,600;1,500;1,600&display=swap">
<style>
:root{
  --bg-deep:#181c2f;
  --bg-raised:#222843;
  --card:#242b4a;
  --card-line:#323a5e;
  --text:#e8e9f2;
  --text-soft:#b5b9d4;
  --text-muted:#9094b8;
  --plum:#9a4c9e;
  --rose:#d08fb0;
  --gold:#f2aa3c;
  --lime:#d6e13a;
  --teal:#3a9fb8;
  --red:#e0474f;
  --serif:"Playfair Display", Georgia, serif;
  --sans:"Inter", Arial, sans-serif;
}
*{box-sizing:border-box;margin:0;padding:0}
html,body{width:1200px;height:4080px;overflow:hidden}
body{background:var(--bg-deep);color:var(--text);font-family:var(--sans);position:relative}
section,header,footer{position:absolute;left:0;width:1200px}
.center{text-align:center;position:absolute;left:0;width:1200px}

/* hero */
.hero{top:0;height:580px;background:radial-gradient(ellipse at 50% 0%,#1f2440 0%,var(--bg-deep) 70%)}
.hero-waves{position:absolute;left:40px;top:190px;width:1120px;height:200px;border-radius:50%;
  background:linear-gradient(90deg,rgba(154,76,158,0) 0%,rgba(154,76,158,.35) 18%,rgba(242,170,60,.35) 40%,rgba(214,225,58,.22) 55%,rgba(58,159,184,.35) 75%,rgba(58,159,184,0) 100%);
  filter:blur(18px);opacity:.8}
.hero-kicker{top:222px;font-family:var(--serif);font-style:italic;color:var(--gold);font-size:16px}
.hero-title{top:255px;font-family:var(--serif);font-weight:600;font-size:58px;color:#fff}
.hero-sub{top:340px;font-size:15px;line-height:23px;color:var(--text)}
.btn-grad{position:absolute;left:50%;transform:translateX(-50%);height:38px;border-radius:19px;
  background:linear-gradient(90deg,var(--teal),#8a5fa6 60%,var(--rose));color:#fff;font-size:12px;font-weight:700;
  letter-spacing:.04em;display:flex;align-items:center;justify-content:center;box-shadow:0 6px 18px rgba(154,76,158,.35)}
.btn-line{position:absolute;left:50%;transform:translateX(-50%);height:38px;border-radius:19px;border:1px solid #4a5178;
  color:#fff;font-size:12px;font-weight:700;letter-spacing:.04em;display:flex;align-items:center;justify-content:center}

/* nav */
.site-nav{top:580px;height:80px;border-bottom:1px solid #262c48}
.brand{position:absolute;left:192px;top:28px;display:flex;align-items:center;gap:6px;font-size:8px;font-weight:600;letter-spacing:.05em;color:var(--text-soft)}
.brand-dot{width:12px;height:12px;border:1px solid var(--text-muted);border-radius:50%}
.nav-links{position:absolute;right:182px;top:30px;display:flex;gap:23px;font-size:11px;font-weight:600;letter-spacing:.03em}
.nav-links a{color:var(--text);text-decoration:none;padding-bottom:8px}
.nav-links a.active{color:#fff;border-bottom:2px solid var(--gold)}
.social{display:flex;gap:12px;align-items:center}
.social span{width:8px;height:8px;border-radius:50%;background:var(--text-soft);display:block}

/* sections */
.intro{top:660px;height:363px;background:var(--bg-raised)}
.discover{top:1023px;height:734px;background:var(--bg-deep)}
.guide{top:1757px;height:665px;background:var(--bg-raised)}
.stories{top:2422px;height:716px;background:var(--bg-deep)}
.insights{top:3138px;height:680px;background:var(--bg-raised)}
.h-serif{font-family:var(--serif);font-size:32px}
.h-plain{color:var(--rose);font-weight:500}
.h-italic{font-style:italic;font-weight:500;color:var(--plum);font-size:38px}
.h-lime{color:var(--lime)}
.lede{font-size:13.5px;line-height:22px;color:var(--text)}

.feature{position:absolute;background:var(--card);border-radius:4px;border-left:3px solid;padding:24px 20px;text-align:center}
.feature h3{font-size:15px;font-weight:700;color:#fff;margin-bottom:12px}
.feature p{font-size:11.5px;line-height:19px;color:var(--text-muted)}

.avatar{position:absolute;left:546px;top:239px;width:108px;height:108px;border-radius:50%;border:3px solid var(--plum);
  background:radial-gradient(circle,#2c3356,#1d2240)}
.guide-name{top:363px;font-weight:700;font-size:15px;color:#fff}
.guide-role{top:386px;font-size:10.5px;font-weight:500;letter-spacing:.05em;color:var(--teal)}
.guide-bio{top:417px;font-size:11.5px;line-height:19px;color:var(--text-muted)}

.quote{position:absolute;left:351px;width:509px;height:127px;background:var(--card);border-left:3px solid var(--gold);border-radius:4px;padding:26px 26px}
.quote p{font-style:italic;font-size:13px;line-height:22px;color:#fff}
.quote cite{display:block;margin-top:16px;font-style:normal;font-weight:700;font-size:12px;color:var(--gold)}

.post{position:absolute;top:215px;width:260px;height:313px;background:var(--card);border:1px solid var(--card-line);border-radius:4px}
.post-image{height:160px;background:linear-gradient(135deg,#2a2f55,#3a2d52)}
.post-body{padding:16px 17px}
.post h3{font-size:13.5px;font-weight:700;line-height:19px;color:#fff;margin-bottom:9px}
.post p{font-size:11px;line-height:18px;color:var(--text-muted)}
.post a{position:absolute;left:17px;bottom:16px;font-size:10.5px;font-weight:600;color:var(--teal);text-decoration:none}

/* footer */
.site-footer{top:3818px;height:262px;background:var(--bg-raised);border-top:1px solid #2c3354}
.news-title{position:absolute;left:192px;top:46px;font-size:14px;font-weight:700;color:#fff}
.news-copy{position:absolute;left:192px;top:72px;width:470px;font-size:11px;line-height:18px;color:var(--text-muted)}
.news-input{position:absolute;left:192px;top:130px;width:365px;height:32px;border:1px solid #3a4166;border-radius:16px;background:#1b2038;
  font-size:11px;color:var(--text-muted);padding:9px 14px}
.news-btn{position:absolute;left:564px;top:130px;width:95px;height:32px;border-radius:16px;background:var(--plum);color:#fff;font-size:11px;font-weight:700;display:flex;align-items:center;justify-content:center}
.footer-quote{position:absolute;right:182px;top:62px;width:320px;text-align:right}
.footer-quote blockquote{font-style:italic;font-size:21px;line-height:30px;color:var(--plum);padding-right:12px;border-right:3px solid var(--plum);text-align:left}
.footer-quote cite{display:block;margin-top:8px;font-size:10px;color:var(--text-soft)}
.footer-rule{position:absolute;left:192px;top:203px;width:826px;border-top:1px solid #343b60}
.copyright{position:absolute;left:192px;top:228px;font-size:10px;color:var(--text-muted)}
.footer-social{position:absolute;right:182px;top:230px}
</style>
</head>
<body>

<section class="hero">
  <div class="hero-waves" role="img" aria-label="Flowing spectrum of colourful energy waves"></div>
  <p class="center hero-kicker">Tom Kessick Presents</p>
  <h1 class="center hero-title">Bloom</h1>
  <p class="center hero-sub">Rewire Your Brain, Release Trauma, and Reclaim Your Life Through<br>Neuroscience, Meditation &amp; Ancient Wisdom</p>
  <div class="btn-grad" style="top:426px;width:257px">LEARN MORE ABOUT THE COURSE</div>
</section>

<header class="site-nav">
  <div class="brand"><span class="brand-dot"></span>TOM KESSICK</div>
  <nav class="nav-links">
    <a class="active">HOME</a><a>ABOUT TOM</a><a>THE PROGRAM</a><a>PACKAGES</a><a>JOURNAL</a><a>FAQS</a><a>CONTACT US</a>
    <div class="social" style="padding-bottom:8px"><span></span><span></span></div>
  </nav>
</header>

<section class="intro">
  <h2 class="center h-serif h-plain" style="top:70px">Unlock Your Innate Healing Potential</h2>
  <p class="center lede" style="top:128px">This transformative program, guided by Tom Kessick - A Pilot Beyond Every Storm -<br>integrates cutting-edge neuroscience with profound meditation practices to help you<br>overcome emotional trauma, heal illness, and activate your mind-body connection for<br>lasting well-being.</p>
  <div class="btn-line" style="top:255px;width:158px">MEET TOM KESSICK</div>
</section>

<section class="discover">
  <h2 class="center h-serif h-italic" style="top:70px">What You’ll Discover in Bloom</h2>
  <p class="center lede" style="top:132px">A comprehensive journey combining scientific understanding with practical techniques for<br>deep, sustainable transformation.</p>
  <div class="feature" style="left:192px;top:217px;width:256px;height:180px;border-color:var(--red)">
    <h3>Neuroplasticity &amp; Rewiring</h3>
    <p>Understand the science of how your brain can change and learn Tom Kessick’s proven methods to create new neural pathways for health and happiness.</p>
  </div>
  <div class="feature" style="left:477px;top:217px;width:256px;height:180px;border-color:var(--gold)">
    <h3>Emotional Healing</h3>
    <p>Address the root causes of emotional stress and disease using powerful techniques like the Silver Lattice Release (SLR) process.</p>
  </div>
  <div class="feature" style="left:762px;top:217px;width:256px;height:180px;border-color:var(--lime)">
    <h3>Meditation &amp; Frequencies</h3>
    <p>Explore the profound effects of meditation and specific Solfeggio frequencies on your mind, body, and spirit, including guided Chakra meditations.</p>
  </div>
  <div class="feature" style="left:192px;top:427px;width:256px;height:162px;border-color:var(--teal)">
    <h3>Mind-Body Integration</h3>
    <p>Deepen your mind-body-spirit connection to unlock intuitive wisdom, reduce physical symptoms, and foster holistic well-being.</p>
  </div>
  <div class="btn-grad" style="top:625px;width:233px">EXPLORE THE FULL PROGRAM</div>
</section>

<section class="guide">
  <h2 class="center h-serif h-italic" style="top:70px">Meet Your Guide</h2>
  <p class="center lede" style="top:132px">Learn directly from Tom Kessick, whose personal journey of profound healing fuels the<br>transformative power of the Bloom course.</p>
  <div class="avatar" role="img" aria-label="Portrait of Tom Kessick"></div>
  <p class="center guide-name">Tom Kessick</p>
  <p class="center guide-role">A PILOT BEYOND EVERY STORM</p>
  <p class="center guide-bio">Tom shares his remarkable story and the<br>scientifically-backed techniques he developed<br>to overcome trauma and illness, empowering<br>you to do the same.</p>
  <div class="btn-line" style="top:556px;width:166px">READ TOM’S STORY</div>
</section>

<section class="stories">
  <h2 class="center h-serif h-italic h-lime" style="top:66px">Transformational Stories</h2>
  <p class="center lede" style="top:131px">Real results from individuals who have experienced profound shifts through the Bloom<br>program.</p>
  <div class="quote" style="top:215px"><p>"Bloom didn’t just change my perspective; it fundamentally changed my health and my life. Tom’s approach is unique and incredibly effective."</p><cite>– Olivia M.</cite></div>
  <div class="quote" style="top:367px"><p>"After years of searching, I finally found the tools to address deep-seated emotional patterns. I feel lighter, clearer, and more empowered."</p><cite>– David R.</cite></div>
  <div class="quote" style="top:518px"><p>"The blend of science and spiritual practice resonated deeply. This course provided the structure and support I needed to truly heal."</p><cite>– Chloe S.</cite></div>
</section>

<section class="insights">
  <h2 class="center h-serif h-italic" style="top:70px">Insights from Tom</h2>
  <p class="center lede" style="top:131px">Explore articles and resources on neuroplasticity, emotional wellness, meditation, and the<br>power of the mind-body connection.</p>
  <article class="post" style="left:192px">
    <div class="post-image" role="img" aria-label="Sunrise image"></div>
    <div class="post-body"><h3>Can You Really Rewire Your Brain?</h3><p>Understanding the science of neuroplasticity and how intentional practice can create lasting change...</p></div>
    <a>Read More →</a>
  </article>
  <article class="post" style="left:475px">
    <div class="post-image" role="img" aria-label="Glowing heart abstract"></div>
    <div class="post-body"><h3>The Hidden Impact of Emotional Stress</h3><p>Exploring the deep connection between unresolved emotions and physical well-being...</p></div>
    <a>Read More →</a>
  </article>
  <article class="post" style="left:758px">
    <div class="post-image" role="img" aria-label="Sprout growing"></div>
    <div class="post-body"><h3>Solfeggio Frequencies: Ancient Sounds, Modern Healing</h3><p>How specific sound frequencies used in the Bloom course can support your journey...</p></div>
    <a>Read More →</a>
  </article>
  <div class="btn-line" style="top:569px;width:172px">VISIT THE JOURNAL</div>
</section>

<footer class="site-footer">
  <h2 class="news-title">Receive Healing Insights</h2>
  <p class="news-copy">Join our community and get resources, course updates, and inspiration delivered to your inbox.</p>
  <div class="news-input">Enter your email</div>
  <div class="news-btn">SUBSCRIBE</div>
  <div class="footer-quote">
    <blockquote>"Your mind is the key. Unlock its potential, heal your body."</blockquote>
    <cite>– Tom Kessick</cite>
  </div>
  <div class="footer-rule"></div>
  <p class="copyright">© 2025 Pine and Lantern Academy. All Rights Reserved.</p>
  <div class="social footer-social"><span></span><span></span></div>
</footer>

</body>
</html>
```